Letterhead/Busines Cards for Harborview Psychiatry, PLLC - modern psychiatric practice
Harborview Psychiatry, PLLC
Professional
Gerald Matthis, MSN, APRN, PMHNP-BC
President
5812 Quailrun Lane
Lexington, KY 40509
tkwarden4@mailvista.example
please design leaving out black background

```html
<!DOCTYPE html>
<html lang="en">
<head>
<meta charset="utf-8">
<title>Harborview Psychiatry, PLLC – Business Card</title>
<link href="https://fonts.googleapis.com/css2?family=Open+Sans:wght@400;600;700&display=swap" rel="stylesheet">
<style>
  :root {
    --page-bg: #e4e1dc;
    --card-bg: #fbfaf7;
    --card-edge: #d9d5ce;
    --gold: #c07f2c;
    --gold-light: #e3a552;
    --gold-dark: #a0601d;
    --text-main: #3a3a3a;
    --icon-ink: #ffffff;
    --silver-light: #f4f4f4;
    --silver-dark: #9a9a9a;
  }
  * { margin: 0; padding: 0; box-sizing: border-box; }
  html, body {
    width: 1200px; height: 902px; overflow: hidden;
    background: var(--page-bg);
    font-family: "Open Sans", Arial, sans-serif;
  }
  .card {
    position: absolute; left: 100px; top: 166px;
    width: 1000px; height: 570px;
    background: var(--card-bg);
    border: 1px solid var(--card-edge);
    border-radius: 6px;
    box-shadow: 0 10px 30px rgba(0,0,0,.18);
    color: var(--text-main);
  }
  .brand {
    position: absolute; top: 96px; left: 0; width: 100%;
    display: flex; justify-content: center; align-items: center; gap: 16px;
  }
  .brand-dot {
    width: 20px; height: 20px; border-radius: 50%; background: var(--gold);
  }
  .brand-name {
    font-size: 40px; font-weight: 700; color: var(--gold); letter-spacing: .5px;
    white-space: nowrap;
  }
  .holder {
    position: absolute; top: 196px; width: 100%; text-align: center;
  }
  .holder-name {
    font-size: 26px; font-weight: 600; color: var(--gold); line-height: 1.3;
  }
  .holder-title {
    font-size: 19px; color: var(--text-main); margin-top: 2px;
  }
  .contacts {
    position: absolute; top: 318px; left: 90px; right: 90px;
    font-size: 17px; color: var(--text-main);
  }
  .contact-row {
    display: flex; justify-content: space-between; align-items: center;
    margin-bottom: 12px; white-space: nowrap;
  }
  .contact-item { display: inline-flex; align-items: center; gap: 8px; margin-right: 20px; }
  .contact-item:last-child { margin-right: 0; }
  .contact-row > .contact-item:last-child { min-width: 280px; }
  .icon { width: 18px; height: 18px; flex: none; }
  .band {
    position: absolute; left: 0; right: 0; top: 420px; height: 48px;
  }
  .band-line {
    position: absolute; top: 14px; height: 18px; width: 38%;
    background: linear-gradient(180deg, var(--silver-light), var(--silver-dark));
  }
  .band-line.left { left: 0; }
  .band-line.right { right: 0; }
  .web-bar {
    position: absolute; left: 24%; right: 24%; top: 0; height: 48px;
    border-radius: 6px;
    background: linear-gradient(180deg, var(--gold-light), var(--gold-dark));
    display: flex; align-items: center; justify-content: center;
    font-size: 18px; letter-spacing: 3.5px; color: #fff; font-weight: 600;
    white-space: nowrap;
  }
</style>
</head>
<body>
  <main class="card">
    <div class="brand">
      <span class="brand-dot"></span>
      <span class="brand-name">Harborview Psychiatry, PLLC</span>
    </div>

    <div class="holder">
      <p class="holder-name">Gerald Matthis,<br>MSN, APRN, PMHNP-BC</p>
      <p class="holder-title">President</p>
    </div>

    <div class="contacts">
      <div class="contact-row">
        <span class="contact-item">
          <svg class="icon" viewBox="0 0 20 20"><circle cx="10" cy="10" r="10" fill="#c07f2c"/><path d="M10 4a4 4 0 0 0-4 4c0 3 4 8 4 8s4-5 4-8a4 4 0 0 0-4-4zm0 5.5a1.5 1.5 0 1 1 0-3 1.5 1.5 0 0 1 0 3z" fill="#ffffff"/></svg>
          5812 Quailrun Lane Lexington, KY 40509
        </span>
        <span class="contact-item">
          <svg class="icon" viewBox="0 0 20 20"><circle cx="10" cy="10" r="10" fill="#c07f2c"/><circle cx="10" cy="10" r="5.5" fill="none" stroke="#ffffff" stroke-width="1.4"/><path d="M4.5 10h11M10 4.5c-2.5 3-2.5 8 0 11M10 4.5c2.5 3 2.5 8 0 11" fill="none" stroke="#ffffff" stroke-width="1.2"/></svg>
          www.harborviewpsych.example
        </span>
      </div>
      <div class="contact-row">
        <span>
          <span class="contact-item">
            <svg class="icon" viewBox="0 0 20 20"><circle cx="10" cy="10" r="10" fill="#c07f2c"/><path d="M7 5l2 3-1.2 1.2a7 7 0 0 0 3 3L12 11l3 2-1 2c-4 0-9-5-9-9z" fill="#ffffff"/></svg>
            (606) 555-0182
          </span>
          <span class="contact-item">
            <svg class="icon" viewBox="0 0 20 20"><circle cx="10" cy="10" r="10" fill="#c07f2c"/><path d="M7 5l2 3-1.2 1.2a7 7 0 0 0 3 3L12 11l3 2-1 2c-4 0-9-5-9-9z" fill="#ffffff"/></svg>
            (606) 555-0147
          </span>
        </span>
        <span class="contact-item">
          <svg class="icon" viewBox="0 0 20 20"><circle cx="10" cy="10" r="10" fill="#c07f2c"/><rect x="5" y="6.5" width="10" height="7" fill="#ffffff"/><path d="M5 6.5l5 4 5-4" fill="none" stroke="#c07f2c" stroke-width="1"/></svg>
          tkwarden4@mailvista.example
        </span>
      </div>
    </div>

    <div class="band">
      <span class="band-line left"></span>
      <span class="band-line right"></span>
      <div class="web-bar">www.harborviewpsych.example</div>
    </div>
  </main>
</body>
</html>
```